Rw construct holdings pty ltd

This is a development and construction company. Website can be set up on our domain rwbuildgroup.net if we could change the domain to rwbuildgroup.com.au would be great

Want the page to have eye catching designs, red, black and white are the preffered colours.

Check out www.tolumine.com.au it is my former company with my partner which i am now venturing out on my own, that is the perfect example of the website i want even allot of the information would be the same

Industry/Entity Type

Construction

Coding

Coded - Design and coding required

Number of Pages Required

5+ page

Requirements
Must have
• Company logo eye catching designs

```html
<!DOCTYPE html>
<html lang="en">
<head>
<meta charset="utf-8">
<title>RW Build – Development &amp; Construction</title>
<link href="https://fonts.googleapis.com/css2?family=Jost:wght@500;600;700&family=Poppins:wght@400;500;600&display=swap" rel="stylesheet">
<style>
:root{
  --red:#f63b3b;
  --red-dark:#e52d2d;
  --black:#111111;
  --ink:#222222;
  --grey:#6d6d6d;
  --white:#ffffff;
  --footer:#1b1b1b;
}
*{margin:0;padding:0;box-sizing:border-box}
html,body{width:1200px;height:3709px;overflow:hidden}
body{position:relative;font-family:"Poppins",sans-serif;color:var(--ink);background:var(--white)}
.abs{position:absolute}
.heading{font-family:"Jost",sans-serif;font-weight:600}
.btn{position:absolute;display:flex;align-items:center;justify-content:center;background:var(--red);color:var(--white);font-size:13px;font-weight:500;text-transform:uppercase}
.rule{position:absolute;height:3px;background:var(--red)}
.photo{position:absolute}

/* hero */
.hero{position:absolute;left:0;top:0;width:1200px;height:638px;background:linear-gradient(100deg,#3a3633 0%,#55504a 45%,#8a8460 75%,#b4a878 100%)}
.hero-shade{position:absolute;inset:0;background:linear-gradient(90deg,rgba(0,0,0,.55),rgba(0,0,0,.05))}
.topbar{position:absolute;left:60px;top:30px;width:1035px;height:59px;background:var(--white)}
.brand{position:absolute;display:flex;align-items:center;gap:8px;font-family:"Poppins",sans-serif;font-weight:600;font-size:16px;letter-spacing:1px;color:var(--black)}
.brand i{width:14px;height:14px;background:var(--red);display:block}
.nav{position:absolute;left:542px;top:52px;display:flex;gap:23px;font-size:12px;color:#555}
.nav .active{color:var(--red)}
.hero-title{position:absolute;left:61px;top:232px;font-size:56px;line-height:61px;color:var(--white)}
.hero-title span{color:var(--red)}
.hero-text{position:absolute;left:61px;top:380px;width:420px;font-size:12.5px;line-height:19.5px;color:var(--white)}

/* about */
.about-title{position:absolute;left:117px;top:722px;font-size:36px;line-height:42px;color:var(--black)}
.body-text{font-size:12.5px;line-height:19.5px;color:var(--grey)}
.step-num{position:absolute;width:67px;height:61px;color:var(--white);font-family:"Jost",sans-serif;font-size:64px;font-weight:500;line-height:61px;text-align:center}
.step-title{position:absolute;font-size:14px;font-weight:500;color:var(--black)}
.step-text{position:absolute;width:220px}

.section-title{position:absolute;left:0;width:1200px;text-align:center;font-size:35px;color:var(--black)}

.project-card{position:absolute;left:375px;top:1490px;width:296px;height:89px;background:var(--white);padding:16px 12px}
.project-card h4{font-size:14px;font-weight:500;color:var(--black);margin-bottom:6px}
.project-card .plus{position:absolute;right:0;bottom:0;width:14px;height:14px;background:var(--red);color:#fff;font-size:12px;line-height:14px;text-align:center}

/* services */
.services{position:absolute;left:0;top:1636px;width:1200px;height:413px;background:var(--red)}
.svc-icon{position:absolute;width:60px;height:60px;border-radius:50%;background:var(--white);display:flex;align-items:center;justify-content:center}
.svc-title{position:absolute;font-size:14px;font-weight:500;color:var(--white)}
.svc-text{position:absolute;width:260px;font-size:12px;line-height:19.5px;color:var(--white)}

/* testimonial */
.stat-big{position:absolute;left:252px;top:2190px;font-size:34px;color:var(--red);font-family:"Jost",sans-serif;font-weight:500}
.stat-label{position:absolute;left:252px;top:2245px;font-size:18px;line-height:26px;color:var(--black);font-weight:500}
.bubble{position:absolute;left:599px;top:2123px;width:300px;height:300px;border-radius:50%;background:var(--black);color:var(--white);text-align:center;padding:108px 42px 0}
.bubble p{font-size:12px;line-height:19.5px}
.bubble .who{color:var(--red);font-size:13.5px;margin-top:12px;font-weight:500}
.avatar{position:absolute;width:60px;height:60px;border-radius:50%;background:linear-gradient(135deg,#b9b2a8,#5a5450);border:2px solid var(--white)}

/* cta */
.cta{position:absolute;left:0;top:2511px;width:1200px;height:190px;background:var(--red)}
.cta h2{position:absolute;left:62px;top:52px;font-size:39px;line-height:46px;color:var(--white)}
.btn-light{background:var(--white);color:var(--red)}

/* news */
.news-caption{position:absolute;left:150px;top:3143px;width:412px;height:48px;background:var(--white);padding:12px 16px 0;font-size:13.5px;line-height:22px;font-weight:500;color:var(--black)}
.author{position:absolute;left:164px;top:3205px;display:flex;align-items:center;gap:10px;font-size:12.5px}
.author .pic{width:38px;height:38px;border-radius:50%;background:linear-gradient(135deg,#c8bfb3,#6b625a)}
.author b{font-weight:500;color:var(--black);font-size:14px;margin-right:12px}
.news-item{position:absolute;left:622px;width:427px;height:92px}
.news-item .thumb{position:absolute;left:0;top:0;width:121px;height:90px}
.news-item .tag{position:absolute;left:144px;top:2px;color:var(--red);font-size:13px}
.news-item h5{position:absolute;left:144px;top:26px;width:280px;font-size:13.5px;line-height:22px;font-weight:500;color:var(--black)}
.news-item .date{position:absolute;left:144px;top:78px;font-size:11px;color:var(--grey)}
.divider{position:absolute;left:622px;width:427px;height:1px;background:#ddd}

/* footer */
.footer{position:absolute;left:0;top:3325px;width:1200px;height:348px;background:var(--footer)}
.f-head{position:absolute;top:3391px;font-size:16px;color:var(--red);font-weight:500}
.f-links{position:absolute;left:337px;top:3424px;list-style:none;font-size:12.5px;color:var(--white);line-height:28.6px}
.f-links li::before{content:"•";color:var(--red);margin-right:12px}
.f-contact{position:absolute;left:612px;display:flex;align-items:center;gap:14px;color:var(--white);font-size:12.5px}
.f-contact .ic{width:30px;height:30px;border-radius:50%;background:var(--white);display:flex;align-items:center;justify-content:center}
.f-input{position:absolute;left:889px;top:3418px;width:251px;height:35px;border-radius:18px;background:var(--white);font-size:11.5px;color:#888;padding:9px 12px}
.copyright{position:absolute;left:0;top:3673px;width:1200px;height:36px;background:var(--red);color:var(--white);font-size:11.5px;text-align:center;line-height:36px}
</style>
</head>
<body>

<!-- Hero -->
<section class="hero">
  <div class="photo" role="img" aria-label="Engineer in hard hat holding rolled blueprints on a building site" style="inset:0;background:linear-gradient(100deg,#3a3633 0%,#5a544c 45%,#8d8562 75%,#b8aa78 100%)"></div>
  <div class="hero-shade"></div>
</section>
<header class="topbar"></header>
<div class="brand" style="left:78px;top:48px"><i></i>RW BUILD</div>
<nav class="nav">
  <span class="active">HOME</span><span>ABOUT US</span><span>SERVICES</span><span>PROJECT</span><span>TESTIMONIALS</span><span>NEWS</span>
</nav>
<a class="btn" style="left:1001px;top:42px;width:139px;height:37px">Contact Us</a>

<h1 class="hero-title heading">RW build and<br><span>construction company</span></h1>
<p class="hero-text">Lorem Ipsum is simply dummy text of the printing and typesetting industry. Lorem Ipsum has been the industry's standard dummy text ever since the 1500s,</p>
<a class="btn" style="left:60px;top:453px;width:139px;height:38px">Contact Us</a>

<!-- About -->
<div class="rule" style="left:117px;top:719px;width:53px"></div>
<h2 class="about-title heading">We Are Deliver &nbsp;High Quality<br>Business</h2>
<p class="abs body-text" style="left:117px;top:810px;width:420px">Lorem Ipsum is simply dummy text of the printing and typesetting industry. Lorem Ipsum has been the industry's standard dummy text ever since the 1500s, &nbsp;when an unknown printer took a galley of type and scrambled it to make a type specimen book.</p>
<a class="btn" style="left:117px;top:905px;width:142px;height:37px">Get a Quote</a>
<div class="abs" role="img" aria-label="Large brand mark in red and black" style="left:667px;top:712px;width:436px;height:226px;background:linear-gradient(135deg,#1b1b1b 0%,#e52d2d 45%,#f63b3b 100%);border-radius:18px"></div>

<div class="step-num" style="left:210px;top:1011px;background:var(--red)">1</div>
<div class="step-num" style="left:496px;top:1011px;background:var(--black)">2</div>
<div class="step-num" style="left:774px;top:1011px;background:var(--red)">3</div>
<div class="step-title" style="left:211px;top:1087px">Find Out Need</div>
<div class="step-title" style="left:497px;top:1087px">Devloping Project</div>
<div class="step-title" style="left:774px;top:1087px">Building a Dream</div>
<p class="step-text body-text" style="left:211px;top:1114px">Lorem Ipsum is simply dummy text of the printing and typesetting industry.</p>
<p class="step-text body-text" style="left:497px;top:1114px">Lorem Ipsum is simply dummy text of the printing and typesetting industry.</p>
<p class="step-text body-text" style="left:774px;top:1114px">Lorem Ipsum is simply dummy text of the printing and typesetting industry.</p>

<!-- Projects -->
<div class="rule" style="left:573px;top:1246px;width:54px"></div>
<h2 class="section-title heading" style="top:1248px">Our Project</h2>
<div class="photo" role="img" aria-label="Construction team reviewing plans on site" style="left:0;top:1302px;width:307px;height:314px;background:linear-gradient(135deg,#9c978c,#c7a868 50%,#4d4a47)"></div>
<div class="photo" role="img" aria-label="Engineer pointing at a crane against a blue sky" style="left:337px;top:1302px;width:526px;height:314px;background:linear-gradient(160deg,#8fb0d6,#c9d8ea 45%,#5e7388)"></div>
<div class="photo" role="img" aria-label="Modern grey concrete house at dusk" style="left:893px;top:1302px;width:307px;height:314px;background:linear-gradient(180deg,#a9bfd2,#c6ccd0 60%,#6b7470)"></div>
<div class="project-card">
  <h4>Devloping Project</h4>
  <p class="body-text" style="font-size:12px">Lorem Ipsum is simply dummy text of the printing and typesetting industry.</p>
  <span class="plus">+</span>
</div>

<!-- Services -->
<section class="services"></section>
<div class="photo" role="img" aria-label="Two construction workers in yellow hard hats" style="left:90px;top:1657px;width:374px;height:374px;border-radius:50%;background:radial-gradient(circle at 55% 45%,#e9c44a 0%,#f0f0f0 40%,#ffffff 70%)"></div>
<div class="rule" style="left:590px;top:1710px;width:53px;background:var(--white)"></div>
<h2 class="abs heading" style="left:590px;top:1712px;font-size:35px;color:var(--white)">Our Services</h2>
<div class="svc-icon" style="left:589px;top:1788px">
  <svg width="30" height="30" viewBox="0 0 30 30" fill="none" stroke="#f63b3b" stroke-width="2"><rect x="4" y="4" width="22" height="22"/><path d="M9 9h12v12H9zM4 14h5M21 16h5"/></svg>
</div>
<div class="svc-icon" style="left:875px;top:1788px">
  <svg width="30" height="30" viewBox="0 0 30 30" fill="none" stroke="#f63b3b" stroke-width="2"><rect x="3" y="5" width="24" height="17"/><path d="M10 26h10M15 22v4M7 10h16M7 15h10"/></svg>
</div>
<div class="svc-title" style="left:590px;top:1863px">Architectural Development</div>
<div class="svc-title" style="left:875px;top:1863px">Engineering &nbsp;Construction</div>
<p class="svc-text" style="left:590px;top:1891px">Lorem Ipsum is simply dummy text of the printing and typesetting industry. Lorem Ipsum has been the industry's standard dummy text ever since the 1500s,</p>
<p class="svc-text" style="left:875px;top:1891px">Lorem Ipsum is simply dummy text of the printing and typesetting industry. Lorem Ipsum has been the industry's standard dummy text ever since the 1500s,</p>

<!-- Testimonial -->
<div class="stat-big">95%</div>
<div class="stat-label">Milions Of<br>Customers &nbsp;Like<br>Our Service</div>
<div class="rule" style="left:252px;top:2334px;width:53px"></div>
<svg class="abs" style="left:570px;top:2181px" width="80" height="70" viewBox="0 0 80 70"><path d="M0 0H80L60 70Z" fill="#111"/></svg>
<div class="bubble">
  <svg width="46" height="38" viewBox="0 0 46 38" style="position:absolute;left:127px;top:55px" fill="#f63b3b"><path d="M0 0h20v20l-8 18H4l6-16H0zM26 0h20v20l-8 18h-8l6-16h-10z"/></svg>
  <p>Lorem Ipsum is simply dummy text of the printing and typesetting industry. Lorem Ipsum has been the industry's standard</p>
  <div class="who">Marta Ellison</div>
  <p>Lorem Ipsum is</p>
</div>
<div class="avatar" role="img" aria-label="Client portrait" style="left:857px;top:2107px;border-color:var(--red)"></div>
<div class="avatar" role="img" aria-label="Client portrait" style="left:903px;top:2168px"></div>
<div class="avatar" role="img" aria-label="Client portrait" style="left:925px;top:2243px"></div>
<div class="avatar" role="img" aria-label="Client portrait" style="left:903px;top:2313px"></div>
<div class="avatar" role="img" aria-label="Client portrait" style="left:857px;top:2370px"></div>

<!-- CTA -->
<section class="cta" role="img" aria-label="Red band over faint architectural drawing"></section>
<h2 class="abs heading" style="left:62px;top:2563px;font-size:39px;line-height:46px;color:var(--white)">We Help Our Client To Achive<br>Their Goals</h2>
<a class="btn btn-light" style="left:1001px;top:2594px;width:139px;height:38px">Contact Us</a>

<!-- News -->
<div class="rule" style="left:575px;top:2775px;width:54px"></div>
<h2 class="section-title heading" style="top:2778px">Latest News</h2>
<div class="photo" role="img" aria-label="Worker in white hard hat using a tablet on site" style="left:150px;top:2855px;width:412px;height:288px;background:linear-gradient(150deg,#d9d2c5,#b9a58b 40%,#6e8f3a 80%,#404a2c)"></div>
<div class="abs" style="left:528px;top:3143px;width:34px;height:28px;background:#777"></div>
<div class="news-caption">Lorem Ipsum is simply dummy text of the<br>printing and typesetting industry.</div>
<div class="author" style="top:3204px">
  <span class="pic" role="img" aria-label="Author portrait"></span>
  <b>Dane Whitfield</b><span style="color:var(--red)">/ Services</span><span style="color:var(--grey);margin-left:6px">/ &nbsp;29 Dec, &nbsp;2021</span>
</div>

<div class="rule" style="left:622px;top:2880px;width:427px;height:2px"></div>
<div class="news-item" style="top:2911px">
  <div class="thumb" role="img" aria-label="House frame model on blueprints" style="background:linear-gradient(135deg,#d6dde4,#b79a74)"></div>
  <span class="tag">News</span><h5>Lorem Ipsum is simply dummy text of the printing and</h5><span class="date">29 Dec , 2021</span>
</div>
<div class="divider" style="top:3015px"></div>
<div class="news-item" style="top:3033px">
  <div class="thumb" role="img" aria-label="Workers in hi-vis vests on site" style="background:linear-gradient(135deg,#4a6a96,#c7c23a 55%,#3b3b3b)"></div>
  <span class="tag">News</span><h5>Lorem Ipsum is simply dummy text of the printing and</h5><span class="date">29 Dec , 2021</span>
</div>
<div class="divider" style="top:3142px"></div>
<div class="news-item" style="top:3159px">
  <div class="thumb" role="img" aria-label="Engineers reviewing plans outdoors" style="background:linear-gradient(135deg,#e4e7ea,#c9a873 55%,#7b6a55)"></div>
  <span class="tag">News</span><h5>Lorem Ipsum is simply dummy text of the printing and</h5><span class="date">29 Dec , 2021</span>
</div>

<!-- Footer -->
<footer class="footer" role="img" aria-label="Dark city skyline backdrop"></footer>
<div class="brand" style="left:59px;top:3416px;color:var(--white)"><i></i>RW BUILD</div>

<div class="f-head" style="left:337px">Site Map</div>
<ul class="f-links">
  <li>Home</li><li>About Us</li><li>Services</li><li>Testimonials</li><li>Project</li><li>News</li><li>Contact Us</li>
</ul>

<div class="f-head" style="left:612px">Contact Us</div>
<div class="f-contact" style="top:3424px"><span class="ic"><svg width="14" height="14" viewBox="0 0 24 24" fill="#f63b3b"><path d="M6.6 10.8a15 15 0 006.6 6.6l2.2-2.2c.3-.3.7-.4 1-.2 1.1.4 2.3.6 3.6.6.6 0 1 .4 1 1V20c0 .6-.4 1-1 1A17 17 0 013 4c0-.6.4-1 1-1h3.5c.6 0 1 .4 1 1 0 1.3.2 2.5.6 3.6.1.3 0 .7-.2 1z"/></svg></span>044-210 555 0198</div>
<div class="f-contact" style="top:3477px"><span class="ic"><svg width="14" height="14" viewBox="0 0 24 24" fill="#f63b3b"><path d="M2 5h20v14H2zM2 5l10 8 10-8" stroke="#fff" stroke-width="1.5"/></svg></span>info@rwbuildgroup.com.au</div>
<div class="f-contact" style="top:3530px"><span class="ic"><svg width="14" height="14" viewBox="0 0 24 24" fill="#f63b3b"><path d="M12 2a7 7 0 00-7 7c0 5 7 13 7 13s7-8 7-13a7 7 0 00-7-7zm0 9.5A2.5 2.5 0 1112 6a2.5 2.5 0 010 5.5z"/></svg></span>421 , Address Line Goes Here</div>
<div class="f-contact" style="top:3582px"><span class="ic"><svg width="14" height="14" viewBox="0 0 24 24" fill="none" stroke="#f63b3b" stroke-width="2"><circle cx="12" cy="12" r="10"/><path d="M2 12h20M12 2c3 3 3 17 0 20M12 2c-3 3-3 17 0 20"/></svg></span>www.rwbuildgroup.com.au</div>

<div class="f-head" style="left:889px">News Letters</div>
<div class="f-input">Enter &nbsp;Email Address....</div>
<a class="btn" style="left:889px;top:3475px;width:140px;height:36px;border-radius:18px;font-size:12px">Subsribe Now</a>

<div class="copyright">©2021 RW BUILD GROUP &nbsp;, All Rights Reserved.</div>

</body>
</html>
```